Trucking company specializing in intermodal containers

We need a logo design for our trucking company based in Kent, Washington. Our companies name is Varnell Haulways LLC, we specialize in intermodal containers, and work off of the Crestmark Rail Lines and the ports. We provide service by transporting freight with our fleet of trucks. We operate within Washington, Oregon, and Idaho. Our fleet consists of an east division and a local division. Our team motto currently is globally connected, locally invested.

Target Market(s)

brokers, intermodal management companies, customers

Industry/Entity Type

Trucking Company

Contact Information for Business Card

physical address 4153 N. 318th Pl Kent, WA 98417
office number is 253-555-0148

Font styles to use
Sans Serif

Colors

Designer to choose colors to be used in the design.

Requirements
Must have
• We need to update our current logo. Something like an emblem; that makes a statement that this logo/ sign represents Varnell Haulways. Something like a royal stamp but in this case a royal shield.
Nice to have
• simple, yet bold. something someone does not currently have. We need something fresh and exciting. Something that will also make a statement because currently our reputation is great within the industry and our community. But we need to reflect that we are professional and willing to provide the best service. We are open to new statement lines.
Should not have
• Should not have something thats been used before. We are open to suggestions that you have and a design that is completely unique and you make originally without what we want but what you like as well. Ofcourse it should still represent the industry we are in.

```html
<!DOCTYPE html>
<html lang="en">
<head>
<meta charset="utf-8">
<title>Varnell Haulways LLC – Business Card</title>
<link href="https://fonts.googleapis.com/css2?family=Open+Sans:wght@400;600;700&display=swap" rel="stylesheet">
<style>
  :root{
    --orange:#d9752f;
    --charcoal:#3b3b3d;
    --slate:#58585b;
    --paper:#ececec;
    --paper-line:#d4d4d4;
    --white:#ffffff;
    --stage:#e2e2e2;
    --W:945px;
    --H:540px;
  }
  *{box-sizing:border-box;margin:0;padding:0}
  html,body{width:1200px;height:1200px;overflow:hidden;background:var(--stage);font-family:"Open Sans",sans-serif}
  .sheet{position:relative;width:1200px;height:1200px}
  .card{
    position:absolute;left:127px;width:var(--W);height:var(--H);overflow:hidden;
    background:var(--paper);
    background-image:repeating-linear-gradient(-45deg,var(--paper) 0 3px,var(--paper-line) 3px 4px);
    box-shadow:0 8px 24px rgba(0,0,0,.18);
  }
  .card--front{top:30px}
  .card--back{top:630px}

  .brand{
    position:absolute;display:flex;flex-direction:column;align-items:center;gap:14px;
    color:var(--orange);font-weight:700;text-align:center;
  }
  .brand__mark{width:26px;height:26px;background:var(--orange)}
  .brand__name{font-size:34px;line-height:1.15;letter-spacing:1px}
  .card--front .brand{left:40px;width:300px;top:200px}
  .card--back .brand{left:110px;width:420px;top:210px}

  .panel{
    position:absolute;inset:0;background:var(--charcoal);
    clip-path:polygon(378px 0,100% 0,100% 100%,510px 100%);
  }
  .band{position:absolute;right:0;left:0;background:var(--orange)}
  .band--top{top:0;height:40px;clip-path:polygon(378px 0,100% 0,100% 100%,388px 100%)}
  .band--bottom{bottom:0;height:38px;clip-path:polygon(500px 0,100% 0,100% 100%,510px 100%)}
  .row{position:absolute;right:0;height:74px;display:flex}
  .row__icon{
    width:78px;height:100%;background:var(--orange);
    display:flex;align-items:center;justify-content:center;
    clip-path:polygon(0 0,88% 0,100% 100%,12% 100%);
  }
  .row__icon svg{width:28px;height:28px;fill:var(--white)}
  .row__bar{
    flex:1;margin-left:6px;background:var(--slate);color:var(--white);
    display:flex;flex-direction:column;justify-content:center;padding-left:44px;
    font-size:20px;line-height:1.3;
    clip-path:polygon(0 0,100% 0,100% 100%,14px 100%);
  }
  .row--address{top:58px;left:398px}
  .row--phone{top:158px;left:420px}
  .row--web{top:258px;left:442px}
  .signature{
    position:absolute;top:362px;left:464px;right:0;height:108px;background:var(--slate);
    clip-path:polygon(0 0,100% 0,100% 100%,20px 100%);
    display:flex;flex-direction:column;justify-content:center;align-items:center;padding-left:20px;
  }
  .signature__name{color:var(--white);font-weight:700;font-size:40px;letter-spacing:6px;line-height:1}
  .signature__tag{color:var(--orange);font-size:22px;letter-spacing:1px;margin-top:6px}

  .back-band{
    position:absolute;inset:0;background:var(--charcoal);
    clip-path:polygon(640px 0,100% 0,100% 100%,760px 100%);
  }
  .back-edge{
    position:absolute;inset:0;background:var(--slate);
    clip-path:polygon(632px 0,640px 0,760px 100%,752px 100%);
  }
  .tagline{
    position:absolute;left:810px;top:255px;width:300px;margin-left:-150px;
    transform:rotate(-90deg);text-align:center;font-size:22px;letter-spacing:1px;color:var(--white);
  }
  .tagline__accent{color:var(--orange)}
</style>
</head>
<body>
<main class="sheet">

  <section class="card card--front" aria-label="Business card front">
    <div class="brand">
      <span class="brand__mark"></span>
      <span class="brand__name">Varnell Haulways LLC</span>
    </div>
    <div class="panel"></div>
    <div class="band band--top"></div>
    <div class="band band--bottom"></div>

    <div class="row row--address">
      <div class="row__icon">
        <svg viewBox="0 0 24 24" aria-hidden="true"><path d="M12 3 2 12h3v8h5v-5h4v5h5v-8h3z"/></svg>
      </div>
      <div class="row__bar"><span>4153 N. 318th Pl Kent,</span><span>WA 98417</span></div>
    </div>

    <div class="row row--phone">
      <div class="row__icon">
        <svg viewBox="0 0 24 24" aria-hidden="true"><path d="M6.6 10.8a15 15 0 0 0 6.6 6.6l2.2-2.2c.3-.3.7-.4 1-.2 1.1.4 2.3.6 3.6.6.6 0 1 .4 1 1V20c0 .6-.4 1-1 1A17 17 0 0 1 3 4c0-.6.4-1 1-1h3.5c.6 0 1 .4 1 1 0 1.3.2 2.5.6 3.6.1.3 0 .7-.2 1z"/></svg>
      </div>
      <div class="row__bar"><span>253 555 0148</span></div>
    </div>

    <div class="row row--web">
      <div class="row__icon">
        <svg viewBox="0 0 24 24" aria-hidden="true"><path d="M12 2a10 10 0 1 0 0 20 10 10 0 0 0 0-20zm6.9 6h-3a15 15 0 0 0-1.3-3.9A8 8 0 0 1 18.9 8zM12 4c.8 1.2 1.5 2.5 1.9 4h-3.8c.4-1.5 1.1-2.8 1.9-4zM4.3 14a8 8 0 0 1 0-4h3.4a16 16 0 0 0 0 4zm.8 2h3a15 15 0 0 0 1.3 3.9A8 8 0 0 1 5.1 16zm3-8h-3a8 8 0 0 1 4.3-3.9C8.8 5.3 8.4 6.6 8.1 8zM12 20c-.8-1.2-1.5-2.5-1.9-4h3.8c-.4 1.5-1.1 2.8-1.9 4zm2.3-6H9.7a14 14 0 0 1 0-4h4.6a14 14 0 0 1 0 4zm.3 5.9c.6-1.2 1-2.5 1.3-3.9h3a8 8 0 0 1-4.3 3.9zm1.7-5.9a16 16 0 0 0 0-4h3.4a8 8 0 0 1 0 4z"/></svg>
      </div>
      <div class="row__bar"><span>info@varnellhaulways.com</span><span>www.varnellhaulways.com</span></div>
    </div>

    <div class="signature">
      <span class="signature__name">VARNELL</span>
      <span class="signature__tag">TRUCKING COMPANY</span>
    </div>
  </section>

  <section class="card card--back" aria-label="Business card back">
    <div class="brand">
      <span class="brand__mark"></span>
      <span class="brand__name">Varnell Haulways LLC</span>
    </div>
    <div class="back-edge"></div>
    <div class="back-band"></div>
    <p class="tagline"><span class="tagline__accent">TRUCKING</span> COMPANY</p>
  </section>

</main>
</body>
</html>
```